Letterhead Design Project

I am the new owner of an existing Accouting and Financial Planning Firm (which I have been an employee at for 3 years)
We need to change the letterhead due to a change to the company's ABN etc., so thought we would like to modernise this at the same time.
We wish to keep the existing logo so there is familiarity to the clients. As per the notes on the attached document, we are happy to remove the wording from the logo, whichever will look better.
The letterhead needs to be professional, yet modern.
I will upload our logo and the required details for the letterhead.

Industry/Entity Type

Financial

Requirements
Must have
• Logo and provided business details.

```html
<!DOCTYPE html>
<html lang="en">
<head>
<meta charset="utf-8">
<title>Kestrel Accountants &amp; Financial Services — Letterhead</title>
<link rel="stylesheet" href="https://fonts.googleapis.com/css2?family=Source+Sans+3:wght@400;700&display=swap">
<style>
  :root {
    --navy: #003a78;
    --amber: #e9a11b;
    --paper: #ffffff;
  }
  html, body {
    margin: 0;
    padding: 0;
    overflow: hidden;
    background: var(--paper);
  }
  .letterhead {
    position: relative;
    width: 849px;
    height: 1200px;
    overflow: hidden;
    background: var(--paper);
    font-family: "Source Sans 3", "Myriad Pro", Arial, sans-serif;
  }
  .frame-rule {
    position: absolute;
  }
  .frame-rule--side-navy { left: 38px; top: 0; width: 13px; height: 1166px; background: var(--navy); }
  .frame-rule--side-amber { left: 51px; top: 0; width: 10px; height: 1154px; background: var(--amber); }
  .frame-rule--base-amber { left: 51px; top: 1142px; right: 0; height: 12px; background: var(--amber); }
  .frame-rule--base-navy { left: 38px; top: 1154px; right: 0; height: 12px; background: var(--navy); }

  .brand {
    position: absolute;
    top: 92px;
    right: 44px;
  }
  .brand__name {
    font-size: 56px;
    font-weight: 700;
    line-height: 1;
    color: var(--navy);
    letter-spacing: -0.5px;
  }

  .contact {
    position: absolute;
    left: 125px;
    top: 1021px;
    width: 660px;
  }
  .contact__company {
    margin: 0 0 8px;
    font-size: 17.5px;
    font-weight: 400;
    color: var(--navy);
  }
  .contact__columns {
    display: flex;
  }
  .contact__column {
    margin: 0;
    padding: 0 0 0 3px;
    list-style: none;
    font-size: 16px;
    line-height: 21px;
    color: var(--amber);
  }
  .contact__column--office { width: 321px; }
</style>
</head>
<body>
<main class="letterhead">
  <div class="frame-rule frame-rule--side-navy"></div>
  <div class="frame-rule frame-rule--side-amber"></div>
  <div class="frame-rule frame-rule--base-amber"></div>
  <div class="frame-rule frame-rule--base-navy"></div>

  <header class="brand">
    <span class="brand__name">Kestrel</span>
  </header>

  <footer class="contact">
    <h1 class="contact__company">Kestrel Accountants &amp; Financial Services</h1>
    <div class="contact__columns">
      <ul class="contact__column contact__column--office">
        <li>ABN: 48 207 316 924</li>
        <li>12 Harlow Street, Marrowby, Vic, 3691</li>
        <li>PO Box 2087, Fenwick, NSW, 2641</li>
      </ul>
      <ul class="contact__column contact__column--reach">
        <li>Ph: 02 5550 1934</li>
        <li>Fax: 02 5550 2648</li>
        <li>Email: office@kestrelaccountants.com.au</li>
        <li>www.kestrelaccountants.com.au</li>
      </ul>
    </div>
  </footer>
</main>
</body>
</html>
```